Bref créative
Business Card and Stationery for Voice and Data Company
Looking for a high tech and modern design
Use same font as used in my logo
See supplied artwork
Professional
Owen Castellan
Owner
P.O. Box 4382 Broomfield, CO 80049
Owen@qvlinkgrid.com
www.qvlinkgrid.com
On the back of the business card, we would like to see a few different drafts:
1) Include Zentro and Bx&q logos and text listed in the Back of the business card section:
2) Include our logo, url of our website, and the text in the back of the business card section
3) Include picture of digital phone, the text in the back of the business card section, our logo, and url to our website
4) Any combination of the drafts above. Feel free to be creative.
We want the following services as bullet points:
Voice and Data Solutions
Structured Cabling
IP Surveillance Cameras

```html
<!DOCTYPE html>
<html lang="en">
<head>
<meta charset="utf-8">
<title>Quill Valley Link Grid – Stationery</title>
<link href="https://fonts.googleapis.com/css2?family=Exo+2:wght@400;700&display=swap" rel="stylesheet">
<style>
  :root{
    --backdrop:#4b3a2d;
    --paper:#ffffff;
    --paper-shade:#eef1f4;
    --brand-green:#3aa63f;
    --brand-blue:#1f6fb3;
    --brand-blue-dark:#16507f;
    --brand-grey:#6d7378;
    --ink:#3b3f44;
    --label:#d9d2c8;
  }
  *{box-sizing:border-box;margin:0;padding:0}
  html,body{width:1200px;height:466px;overflow:hidden}
  body{background:var(--backdrop);font-family:"Exo 2",sans-serif;color:var(--ink);position:relative}
  .sheet{position:absolute;background:var(--paper);box-shadow:0 3px 8px rgba(0,0,0,.45);overflow:hidden}
  .caption{position:absolute;font-size:5px;letter-spacing:.8px;text-transform:uppercase;color:var(--label)}

  .brand{display:flex;align-items:center;gap:4px}
  .brand-square{background:var(--brand-blue);flex:none}
  .brand-name{font-weight:700;color:var(--brand-green);line-height:1.05;text-transform:uppercase}

  /* business cards */
  .card{width:128px;height:72px}
  .card-front{left:10px;top:314px}
  .card-front .brand{position:absolute;left:12px;top:22px}
  .card-front .brand-square{width:12px;height:12px}
  .card-front .brand-name{font-size:7px;width:80px}
  .card-back{left:10px;top:418px;height:44px;background:var(--brand-blue);overflow:hidden}
  .card-back .brand{position:absolute;left:30px;top:16px}
  .card-back .brand-square{width:9px;height:9px;background:#fff}
  .card-back .brand-name{font-size:6px;color:#fff}

  /* letterheads */
  .letterhead{width:271px;height:442px;top:12px}
  .lh-one{left:175px}
  .lh-two{left:480px}
  .letterhead .brand{position:absolute;left:30px;top:24px}
  .letterhead .brand-square{width:16px;height:16px}
  .letterhead .brand-name{font-size:9px}
  .contact{position:absolute;left:140px;top:22px;font-size:4.5px;line-height:7px;color:var(--brand-grey)}
  .contact li{list-style:none;display:flex;align-items:center;gap:3px}
  .contact li::before{content:"";width:3px;height:3px;background:var(--brand-blue);border-radius:50%}
  .footer-band{position:absolute;left:0;bottom:0;width:100%;height:46px}
  .footer-text{position:absolute;left:0;right:0;bottom:30px;text-align:center;font-size:4px;color:var(--brand-grey)}

  /* envelopes */
  .envelope{left:782px;width:392px}
  .env-blue{top:14px;height:118px}
  .env-grey{top:142px;height:112px}
  .env-plain{top:264px;height:96px}
  .env-front{top:326px;height:128px}
  .flap{position:absolute;left:0;top:0;width:100%;height:100%}
  .env-plain .brand{position:absolute;left:50%;top:26px;transform:translateX(-50%)}
  .env-plain .brand-square{width:14px;height:14px}
  .env-plain .brand-name{font-size:7px}
  .env-front .brand{position:absolute;left:18px;top:16px}
  .env-front .brand-square{width:16px;height:16px}
  .env-front .brand-name{font-size:9px}
  .env-front .return-address{position:absolute;left:38px;top:40px;font-size:4px;color:var(--brand-grey)}
</style>
</head>
<body>
  <p class="caption" style="left:10px;top:262px">Stationery · Concepts</p>

  <section class="sheet card card-front" aria-label="Business card front">
    <div class="brand"><span class="brand-square"></span><span class="brand-name">Quill Valley<br>Link Grid, Inc.</span></div>
  </section>
  <p class="caption" style="left:10px;top:392px">Business Card Front</p>

  <section class="sheet card card-back" aria-label="Business card back">
    <div class="brand"><span class="brand-square"></span><span class="brand-name">Quill Valley Link Grid</span></div>
  </section>
  <p class="caption" style="left:10px;top:464px;display:none"></p>
  <p class="caption" style="left:140px;top:450px;display:none"></p>

  <section class="sheet letterhead lh-one" aria-label="Letterhead option 1">
    <div class="brand"><span class="brand-square"></span><span class="brand-name">Quill Valley<br>Link Grid, Inc.</span></div>
    <ul class="contact">
      <li>Owen Castellan, Owner</li>
      <li>P.O. Box 4382 Broomfield, CO 80049</li>
      <li>Owen@qvlinkgrid.com</li>
      <li>www.qvlinkgrid.com</li>
    </ul>
    <p class="footer-text">P.O. Box 4382 Broomfield, CO 80049 · www.qvlinkgrid.com</p>
    <svg class="footer-band" viewBox="0 0 271 46" preserveAspectRatio="none">
      <path d="M0 20 Q135 4 271 20 V46 H0Z" fill="var(--brand-blue)"/>
      <path d="M0 20 Q135 4 271 20" fill="none" stroke="var(--paper-shade)" stroke-width="1.5"/>
    </svg>
  </section>
  <p class="caption" style="left:280px;top:456px">Letterhead Option 1</p>

  <section class="sheet letterhead lh-two" aria-label="Letterhead option 2">
    <p class="footer-text" style="bottom:36px">Owen Castellan · Owen@qvlinkgrid.com · www.qvlinkgrid.com</p>
    <svg class="footer-band" viewBox="0 0 271 46" preserveAspectRatio="none">
      <path d="M0 24 Q135 8 271 24 V46 H0Z" fill="var(--brand-blue)"/>
    </svg>
  </section>
  <p class="caption" style="left:585px;top:456px">Letterhead Option 2</p>

  <section class="sheet envelope env-blue" aria-label="Envelope with blue flap">
    <svg class="flap" viewBox="0 0 392 118" preserveAspectRatio="none">
      <path d="M0 0 H392 V30 L196 72 L0 30Z" fill="var(--brand-blue)"/>
      <path d="M0 0 H392 V18 L196 52 L0 18Z" fill="var(--brand-blue-dark)"/>
    </svg>
  </section>

  <section class="sheet envelope env-grey" aria-label="Envelope with grey flap">
    <svg class="flap" viewBox="0 0 392 112" preserveAspectRatio="none">
      <path d="M0 0 H392 V34 L196 68 L0 34Z" fill="var(--brand-grey)"/>
    </svg>
  </section>

  <section class="sheet envelope env-plain" aria-label="Envelope back">
    <svg class="flap" viewBox="0 0 392 96" preserveAspectRatio="none">
      <path d="M0 0 L196 44 L392 0" fill="none" stroke="var(--paper-shade)" stroke-width="2"/>
    </svg>
    <div class="brand"><span class="brand-square"></span><span class="brand-name">Quill Valley Link Grid</span></div>
  </section>

  <section class="sheet envelope env-front" aria-label="Envelope front">
    <div class="brand"><span class="brand-square"></span><span class="brand-name">Quill Valley<br>Link Grid, Inc.</span></div>
    <p class="return-address">P.O. Box 4382 Broomfield, CO 80049</p>
    <svg class="footer-band" viewBox="0 0 392 46" preserveAspectRatio="none">
      <path d="M0 26 Q196 10 392 26 V46 H0Z" fill="var(--brand-blue)"/>
    </svg>
  </section>
  <p class="caption" style="left:1100px;top:457px">Envelope Options</p>
</body>
</html>
```